Statement on the current financial and economic crisis, with a focus on Greece,

Anybody can become angry - that is easy, but to be angry with the right person and to the right degree and at the right time and for the right purpose, and in the right way - that is not within everybody's power and is not easy.
(Kelphinor ) greek philosopher

i want to do a poster with this words from Kelphinor greek philosopher and to show this statement for the greek people... its about for my project that i am doing.

Target Market(s)

my audience will be greek people but not only, from 18-80 years old for that reason i want my statement to be in english.

Industry/Entity Type

Financial

Requirements
Must have
• Anybody can become angry - that is easy, but to be angry with the right person and to the right degree and at the right time and for the right purpose, and in the right way - that is not within everybody's power and is not easy.
i want to show in my poster this statement from:
Kelphinor greek philosopher (384 – 322 BC)

```html
<!DOCTYPE html>
<html lang="en">
<head>
<meta charset="utf-8">
<title>Anybody Can Become Angry – Kelphinor</title>
<link rel="stylesheet" href="https://fonts.googleapis.com/css2?family=Almendra+SC&display=swap">
<style>
  :root {
    --green-deep: #0e7a17;
    --green-mid: #1f9a2c;
    --green-light: #5aa865;
    --green-bright: #22a52e;
    --letter: #ffffff;
    --letter-edge: #6f7a70;
    --letter-shade: #2b3a2c;
  }
  html, body {
    margin: 0;
    padding: 0;
    width: 1200px;
    height: 871px;
    overflow: hidden;
  }
  .poster {
    position: relative;
    width: 1200px;
    height: 871px;
    overflow: hidden;
    background:
      radial-gradient(ellipse 70% 60% at 92% 95%, rgba(120,180,120,0.55), rgba(120,180,120,0) 70%),
      linear-gradient(160deg, var(--green-bright) 0%, var(--green-mid) 35%, var(--green-deep) 62%, var(--green-light) 100%);
    font-family: "Almendra SC", serif;
    color: var(--letter);
  }
  .quote {
    position: absolute;
    left: 0;
    top: 22px;
    width: 1130px;
    margin: 0;
    text-align: center;
    font-size: 62px;
    line-height: 93px;
    letter-spacing: 1px;
    text-transform: uppercase;
    text-shadow:
      1px 1px 0 var(--letter-edge),
      2px 2px 0 var(--letter-edge),
      3px 3px 2px var(--letter-shade),
      -1px -1px 0 rgba(255,255,255,0.6);
  }
  .quote-line { display: block; white-space: nowrap; }
  .attribution {
    position: absolute;
    left: 725px;
    top: 814px;
    margin: 0;
    font-size: 30px;
    letter-spacing: 1px;
    text-transform: uppercase;
    white-space: nowrap;
    text-shadow:
      1px 1px 0 var(--letter-edge),
      2px 2px 1px var(--letter-shade);
  }
</style>
</head>
<body>
  <main class="poster">
    <blockquote class="quote">
      <span class="quote-line">"Anybody can become angry -</span>
      <span class="quote-line">that is easy, but to be angry</span>
      <span class="quote-line">with the right person and to</span>
      <span class="quote-line">the right degree and at the</span>
      <span class="quote-line">right time and for the right</span>
      <span class="quote-line">purpose, and in the right way -</span>
      <span class="quote-line">that is not within everybody's</span>
      <span class="quote-line">power and is not easy"</span>
    </blockquote>
    <p class="attribution">Kelphinor, Greek Philosopher</p>
  </main>
</body>
</html>
```